Soziale Betreuung für Senioren, die von Herzen kommt!
Zielgruppe
Betreuung von Senioren (keine Pflege) mit den 3 Schwerpunkten „Miteinander reden“, „im Alltag unterstützen“ und „Freizeit gestalten“
Aufgabenstellung
Entwicklung eines Flyers als Hauptwerbemedium, das Interesse bei den Senioren weckt (große
Buchstaben für den Teil, der sich an die Senioren richtet) und auch die Angehörigen überzeugt.
DIN A4 Lang 6-seitig Wickelfalz.

```html
<!DOCTYPE html>
<html lang="de">
<head>
<meta charset="utf-8">
<title>Soziale Betreuung für Senioren – Flyer DIN lang</title>
<link href="https://fonts.googleapis.com/css2?family=Libre+Baskerville:ital,wght@0,400;0,700;1,400&display=swap" rel="stylesheet">
<style>
  :root {
    --paper: #efeadb;
    --teal: #3fb0c2;
    --red: #d61f1f;
    --ink: #2b2b2b;
    --muted: #5a5650;
    --stage: #9a9a9a;
    --photo-skin: #c9a58f;
    --photo-grey: #d8d8d8;
  }
  * { box-sizing: border-box; margin: 0; padding: 0; }
  html, body { width: 1200px; height: 800px; overflow: hidden; }
  body {
    background: linear-gradient(160deg, #b3b3b3, #8c8c8c);
    font-family: "Libre Baskerville", "Times New Roman", serif;
    color: var(--ink);
    position: relative;
  }
  .spread {
    position: absolute; top: 190px; width: 582px; height: 412px;
    display: flex; background: var(--paper);
    box-shadow: 0 8px 24px rgba(0,0,0,.3);
  }
  .spread--outside { left: 12px; }
  .spread--inside { left: 606px; }
  .panel { position: relative; width: 194px; height: 100%; overflow: hidden; border-right: 1px solid rgba(0,0,0,.06); }
  .panel:last-child { border-right: none; }
  .panel--wide { width: 388px; }
  .photo { position: absolute; }
  .heading {
    font-weight: 700; letter-spacing: .08em; font-size: 15px;
    border-bottom: 3px solid var(--teal); display: inline-block; padding-bottom: 1px;
  }
  .small { font-size: 6.3px; line-height: 1.5; letter-spacing: .05em; }
  .accent { color: var(--red); font-weight: 700; }
  .brand {
    position: absolute; font-size: 9px; font-weight: 700; color: var(--teal);
    letter-spacing: .06em; display: flex; align-items: center; gap: 4px;
  }
  .brand::before { content: ""; width: 9px; height: 9px; border-radius: 50%; background: var(--teal); }

  /* Angebot */
  .offer__photo { left: 14px; top: 0; width: 166px; height: 142px; background: linear-gradient(180deg, #8a8f96, #b9c2cc); }
  .offer__body { position: absolute; left: 14px; top: 150px; right: 12px; }
  .offer__body .heading { font-style: italic; font-size: 16px; margin-bottom: 5px; }
  .offer__body p { margin-bottom: 5px; font-style: italic; }

  /* Kontakt */
  .contact__name { position: absolute; left: 0; right: 0; top: 80px; text-align: center; font-size: 16px; font-weight: 700; color: var(--teal); letter-spacing: .08em; }
  .contact__heading { position: absolute; left: 40px; top: 150px; font-size: 18px; }
  .contact__list { position: absolute; left: 16px; top: 196px; right: 8px; list-style: none; }
  .contact__list li { display: flex; align-items: flex-start; gap: 10px; margin-bottom: 12px; font-size: 7px; letter-spacing: .08em; line-height: 1.4; }
  .contact__list svg { flex: none; width: 13px; height: 13px; }

  /* Titel */
  .cover__title { position: absolute; left: 14px; right: 10px; top: 14px; color: var(--muted); letter-spacing: .14em; }
  .cover__title .l1 { font-size: 17px; }
  .cover__title .l2 { font-size: 10px; text-align: right; margin-top: 3px; }
  .cover__title .l3 { display: flex; justify-content: space-between; align-items: center; font-size: 12px; margin-top: 6px; }
  .cover__photo { left: 0; top: 112px; width: 194px; height: 150px; background: linear-gradient(135deg, var(--photo-grey), var(--photo-skin) 55%, var(--photo-grey)); }
  .ticks { position: absolute; left: 10px; top: 280px; list-style: none; }
  .ticks li { display: flex; align-items: center; gap: 6px; font-size: 11px; letter-spacing: .1em; margin-bottom: 8px; }
  .ticks svg { width: 18px; height: 16px; flex: none; }

  /* Innen */
  .relatives { padding: 14px 12px; }
  .relatives .heading { font-size: 11px; margin-bottom: 6px; }
  .relatives p { margin-bottom: 6px; }
  .topic { position: absolute; }
  .topic .heading { font-size: 14px; }
  .topic__text { font-size: 8.5px; line-height: 1.45; letter-spacing: .07em; margin-top: 4px; }
  .topic__head { display: flex; align-items: center; gap: 5px; }
  .topic__head svg { width: 18px; height: 16px; }
  .inner-photo { border-radius: 2px; }
  .costs { position: absolute; left: 14px; right: 14px; bottom: 12px; display: flex; gap: 10px; align-items: flex-start; }
  .costs .heading { font-size: 12px; }
</style>
</head>
<body>

<svg width="0" height="0" style="position:absolute">
  <defs>
    <symbol id="tick" viewBox="0 0 20 16"><path d="M1 8 L7 14 L19 1" fill="none" stroke="#d61f1f" stroke-width="2.6" stroke-linecap="round" stroke-linejoin="round"/></symbol>
  </defs>
</svg>

<!-- Außenseite -->
<section class="spread spread--outside">
  <article class="panel offer">
    <div class="photo offer__photo" role="img" aria-label="Porträtfoto der Betreuerin"></div>
    <div class="offer__body">
      <h2 class="heading">Mein Angebot</h2>
      <p class="small"><b>Was ist eigentlich soziale Betreuung?</b></p>
      <p class="small">Lieber Interessent,</p>
      <p class="small">es freut mich, dass Sie sich Zeit für dieses Informationsblatt nehmen.</p>
      <p class="small">In meiner Dienstleistung geht es um „soziale Betreuung“, die dazu beitragen soll, den Alltag zu strukturieren, zu begleiten und mehr Lebensfreude zu gewinnen.</p>
      <p class="small">Ich, Renate Valberg, möchte Ihnen in dieser Informationsschrift mehr darüber erzählen.</p>
      <p class="small">Herzlich Ihre</p>
    </div>
  </article>

  <article class="panel contact">
    <div class="contact__name">Herzenszeit</div>
    <h2 class="heading contact__heading">Kontakt</h2>
    <ul class="contact__list">
      <li><svg viewBox="0 0 14 14"><rect x="1" y="3" width="12" height="8" fill="none" stroke="#d61f1f"/><path d="M1 3 L7 8 L13 3" fill="none" stroke="#d61f1f"/></svg><span>Renate Valberg<br>Lindenweg 12<br>58300 Wetterfeld</span></li>
      <li><svg viewBox="0 0 14 14"><circle cx="7" cy="7" r="6" fill="none" stroke="#d61f1f"/><path d="M5 4 Q4 8 8 10" fill="none" stroke="#d61f1f" stroke-width="1.5"/></svg><span>02301 / 45 67 89</span></li>
      <li><svg viewBox="0 0 14 14"><rect x="4" y="1" width="6" height="12" rx="1" fill="none" stroke="#d61f1f"/><line x1="6" y1="11" x2="8" y2="11" stroke="#d61f1f"/></svg><span>0170 / 12 34 56 78</span></li>
      <li><svg viewBox="0 0 14 14"><text x="7" y="11" text-anchor="middle" font-size="12" fill="#d61f1f">@</text></svg><span>info@seniorenhilfe-wetterfeld.de</span></li>
      <li><svg viewBox="0 0 14 14"><circle cx="7" cy="7" r="6" fill="none" stroke="#d61f1f"/><ellipse cx="7" cy="7" rx="2.5" ry="6" fill="none" stroke="#d61f1f"/><line x1="1" y1="7" x2="13" y2="7" stroke="#d61f1f"/></svg><span>www.seniorenhilfe-wetterfeld.de</span></li>
    </ul>
  </article>

  <article class="panel cover">
    <svg style="position:absolute;left:0;top:0" width="194" height="412">
      <rect x="0" y="4" width="194" height="4" fill="var(--teal)"/>
      <path d="M0 108 Q97 128 194 112" fill="none" stroke="var(--teal)" stroke-width="4"/>
      <path d="M0 262 Q97 248 194 272" fill="none" stroke="var(--teal)" stroke-width="4"/>
      <rect x="0" y="404" width="194" height="4" fill="var(--teal)"/>
    </svg>
    <div class="photo cover__photo" role="img" aria-label="Foto: junge Hand hält die Hand eines älteren Menschen"></div>
    <div class="cover__title">
      <div class="l1">Soziale Betreuung</div>
      <div class="l2">für Senioren,</div>
      <div class="l3"><span>die von</span>
        <svg width="34" height="30" viewBox="0 0 34 30"><path d="M17 28 C4 18 1 12 1 8 A7 7 0 0 1 17 6 A7 7 0 0 1 33 8 C33 12 30 18 17 28 Z" fill="#e0141b" stroke="#111" stroke-width="1"/></svg>
        <span>kommt!</span></div>
    </div>
    <ul class="ticks">
      <li><svg><use href="#tick"/></svg>Miteinander reden</li>
      <li><svg><use href="#tick"/></svg>Im Alltag unterstützen</li>
      <li><svg><use href="#tick"/></svg>Freizeit gestalten</li>
    </ul>
    <div class="brand" style="right:12px;bottom:14px">Herzenszeit</div>
  </article>
</section>

<!-- Innenseite -->
<section class="spread spread--inside">
  <article class="panel relatives">
    <h2 class="heading">Info für Angehörige</h2>
    <p class="small">Ich unterstütze Ihre Angehörigen so, wie es für alle angenehm ist.</p>
    <p class="small"><span class="accent">Weniger Sorgen</span><br>Als Angehöriger steht man vor besonderen Herausforderungen gestellt. Schon ein plötzlich notwendiger Arztbesuch der Eltern/Grosseltern bringt den Zeitplan ins Wanken.</p>
    <p class="small">-Ich begleite die Senioren zum Arzt, auf Wunsch bis ins Behandlungszimmer!</p>
    <p class="small"><span class="accent">Mehr Zeit für die schönen Dinge</span><br>In der täglichen Routine gerät man leicht in Streit. Während man selbst unter permanentem Zeitdruck leidet, haben Senioren häufig ein anderes Zeitempfinden.</p>
    <p class="small">-Gewinnen Sie mehr gemeinsame Zeit für die schönen Dinge miteinander!</p>
    <p class="small"><span class="accent">Unterstützung durch eine weitere Bezugsperson</span><br>Wie empfinden die Senioren die Unterstützung eines Dritten?<br>-Der neue Kontakt mit weiteren Bezugspersonen wird sehr häufig als Bereicherung empfunden.</p>
    <p class="small">Sofern ein Angehöriger an Demenz erkrankt ist, ist professionelle Hilfe, Unterstützung und Beratung gefragt. -Ich unterstütze Sie gern!</p>
    <p class="small">Ich bin zertifizierte Demenzbegleiterin.</p>
  </article>

  <article class="panel panel--wide">
    <div class="topic" style="left:14px;top:14px;width:220px">
      <div class="topic__head"><svg><use href="#tick"/></svg><h2 class="heading">Miteinander reden</h2></div>
      <p class="topic__text">Zeit für gemeinsame Gespräche, ohne Eile, ohne Hektik. Respekt, Vertrauen und Nächstenliebe.<br><span class="accent">Das ist mein Versprechen an Sie!</span><br>Gespräche über das, was Sie bewegt, oder einfach über Dinge lachen.</p>
    </div>
    <div class="photo inner-photo" style="left:246px;top:16px;width:128px;height:84px;background:linear-gradient(135deg,#b86d3c,#6f7c8c)" role="img" aria-label="Foto: Seniorin im Herbstpark"></div>

    <div class="topic" style="left:14px;top:128px;width:360px">
      <div class="topic__head"><svg><use href="#tick"/></svg><h2 class="heading">Im Alltag unterstützen</h2></div>
      <div style="display:flex;gap:10px;margin-top:4px">
        <div class="photo inner-photo" style="position:relative;flex:none;width:120px;height:78px;background:linear-gradient(135deg,#6a7a9a,#c7494c)" role="img" aria-label="Foto: Seniorin beim Versorgen von Kaninchen"></div>
        <p class="topic__text" style="margin-top:0">Ich unterstütze Sie gern darin, den Haushalt zusammen mit Ihnen zu organisieren. Ein schönes Gefühl, vieles noch selbst zu schaffen. Mit ein wenig Unterstützung:<br><span class="accent">Mehr Mobilität und Sicherheit für Sie!</span></p>
      </div>
    </div>

    <div class="topic" style="left:14px;top:236px;width:230px">
      <div class="topic__head"><svg><use href="#tick"/></svg><h2 class="heading">Freizeit gestalten</h2></div>
      <p class="topic__text">Schönes erleben, in einem nicht alltäglichen Umfeld. Eine Auszeit, um neue Kraft zu finden.<br><span class="accent">Sich auf etwas freuen, etwas vorhaben.</span><br>Wenn Sie es wünschen, auch gern bei Ihnen zu Hause.</p>
    </div>
    <div class="photo inner-photo" style="left:256px;top:232px;width:118px;height:88px;background:linear-gradient(160deg,#5f8f4e,#c9b89a)" role="img" aria-label="Foto: zwei Seniorinnen im Freien"></div>

    <div class="costs">
      <h2 class="heading">Kosten:</h2>
      <p class="small">Ich arbeite allein und ohne administrative Verwaltung oder repräsentative Geschäftsräume. Diesen Kostenvorteil gebe ich an Sie weiter. Auch der Einsatz meines PKWs erfolgt in aller Regel ohne gesonderte Berechnung. Kann in vielen Fällen über die Pflegeversicherung abgerechnet werden. <span class="accent">Sprechen Sie mich gern unverbindlich an.</span></p>
    </div>
  </article>
</section>

</body>
</html>
```